TAVRO Capital Group LLC a High Risk Big Rewards company for Rich Young Entrepreneurs

We would like a very modern, powerful in the eyes of our customers, modern, minimalist feel, financial gain. this business card is for young Rich entrepreneurs who want to invest money into High Risk, Big Rewards Businesses. The card Should sell the business!! let your creativity go Wild! I pick most of the designers for this project because of your BOLD Designs, I would like this card to be Bold, Modern, Minimalist, use as many effects in your graphic Artist Mind, Do not let the Financial sound of this business to make you think Conservative that's the last thing we are! if you have a lot of money and you want to play a risky market call US
Updates

Project Deadline Extended
Reason: have not received, enough designs to choose 1st and second place, sure I have received over 100 designs but it seems most designers are submitting every card they have ever made before and calling it mine, please we are looking for fresh ideas please!

Target Market(s)

Private Risky Investors

Industry/Entity Type

Financial

Contact Information for Business Card

powerful in the eyes of our customers,modern, minimalist feel

Font styles to use
Other font styles liked:
• Modern feeling fonts

Requirements
Must have
• The Company Name is TAVRO Capital Group LLC and it must be on the CARD
• My Name, title, Cell , email
• Delvin Ashcroft G.E.D.
• Managing Member
• 555.038.6195
• delvin@tavrocapitalgroup.example
Nice to have
• try a black thick plastic card with round corners with Delvin Ashcroft GED (make sure GED is smaller than name) just on one side of the card, and my phone number with out the icons and email on the other side, this card should look like a exclusive credit card or exclusive VIP card, something you would never loose

```html
<!DOCTYPE html>
<html lang="en">
<head>
<meta charset="UTF-8">
<title>TAVRO Capital Group LLC — Business Card</title>
<link rel="stylesheet" href="https://fonts.googleapis.com/css2?family=Exo+2:wght@300;400;500;600&family=Orbitron:wght@400&display=swap">
<style>
  :root {
    --bg: #d8d4cf;
    --card-base: #1c1c1d;
    --card-light: #3a3a3c;
    --card-dark: #0f0f10;
    --silver: #d7d7d9;
    --silver-soft: #b9b9bc;
    --muted: #a7a7aa;
    --band-dark: #0a0a0a;
    --band-mid: #1f1f20;
    --white: #ffffff;
    --ink: #1a1a1a;
  }
  * { margin: 0; padding: 0; box-sizing: border-box; }
  html, body {
    width: 1200px; height: 1000px; overflow: hidden;
    background: var(--bg);
    font-family: "Exo 2", "Segoe UI", sans-serif;
  }
  .stage { position: relative; width: 1200px; height: 1000px; }

  .card {
    position: absolute; left: 258px; width: 680px; height: 406px;
    border-radius: 24px; overflow: hidden;
    background:
      radial-gradient(ellipse 70% 60% at 65% 28%, rgba(255,255,255,0.16), rgba(255,255,255,0) 70%),
      repeating-linear-gradient(0deg, rgba(255,255,255,0.018) 0 1px, rgba(0,0,0,0.03) 1px 2px),
      linear-gradient(160deg, var(--card-light) 0%, var(--card-base) 45%, var(--card-dark) 100%);
    box-shadow: 0 10px 22px rgba(0,0,0,0.35);
  }
  .card-front { top: 60px; }
  .card-back { top: 530px; }

  .brand-name {
    position: absolute;
    font-family: "Exo 2", sans-serif;
    font-weight: 600; font-size: 30px; line-height: 1.1;
    color: var(--silver); letter-spacing: 0.04em;
    width: 300px; text-align: center;
  }
  .card-front .brand-name { left: 28px; top: 38px; }
  .card-back .brand-name { left: 30px; top: 282px; width: 260px; font-size: 27px; }

  .front-phone {
    position: absolute; left: 34px; top: 278px;
    font-family: "Orbitron", sans-serif; font-size: 34px;
    color: var(--silver); letter-spacing: 0.42em;
  }
  .holder-name {
    position: absolute; left: 35px; top: 322px;
    font-size: 22px; font-weight: 400; color: var(--silver-soft);
  }
  .holder-name .credential { font-size: 15px; letter-spacing: 0.04em; }
  .holder-title {
    position: absolute; left: 35px; top: 350px;
    font-size: 19px; font-weight: 300; color: var(--muted);
  }

  .inquiry {
    position: absolute; top: 40px; left: 0; width: 100%;
    text-align: center; font-size: 17px; font-weight: 300;
    color: var(--muted); letter-spacing: 0.04em;
  }
  .inquiry svg { vertical-align: -2px; margin: 0 8px 0 6px; }

  .tagline-band {
    position: absolute; top: 72px; left: 0; width: 100%; height: 50px;
    background: linear-gradient(180deg, var(--band-dark), var(--band-mid) 50%, var(--band-dark));
    display: flex; align-items: center; justify-content: center; gap: 20px;
  }
  .tagline { font-size: 21px; color: var(--white); letter-spacing: 0.03em; }

  .signature-labels {
    position: absolute; left: 267px; top: 162px; width: 381px;
    display: flex; justify-content: space-between;
    font-size: 14px; font-weight: 300; color: var(--muted);
  }
  .signature-strip {
    position: absolute; left: 267px; top: 185px; width: 381px; height: 60px;
    background: var(--white);
  }

  .back-contact {
    position: absolute; right: 32px; top: 326px;
    text-align: right; font-size: 18px; font-weight: 300;
    color: var(--silver-soft); line-height: 1.3;
  }
</style>
</head>
<body>
<main class="stage">
  <section class="card card-front" aria-label="Card front">
    <div class="brand-name">TAVRO Capital Group LLC</div>
    <div class="front-phone">555.038.6195</div>
    <div class="holder-name">Delvin Ashcroft <span class="credential">G.E.D</span></div>
    <div class="holder-title">Managing Member</div>
  </section>

  <section class="card card-back" aria-label="Card back">
    <p class="inquiry">For More inquiry Pease Call
      <svg width="14" height="14" viewBox="0 0 24 24" aria-hidden="true"><path fill="#a7a7aa" d="M6.6 10.8c1.4 2.8 3.8 5.1 6.6 6.6l2.2-2.2c.3-.3.7-.4 1-.2 1.1.4 2.3.6 3.6.6.6 0 1 .4 1 1V20c0 .6-.4 1-1 1C10.6 21 3 13.4 3 4c0-.6.4-1 1-1h3.5c.6 0 1 .4 1 1 0 1.3.2 2.5.6 3.6.1.3 0 .7-.2 1z"/></svg>555.038.6195</p>

    <div class="tagline-band">
      <svg width="16" height="26" viewBox="0 0 16 26" aria-hidden="true"><path d="M0 0 L16 13 L0 26 Z" fill="#bcbcbf"/></svg>
      <span class="tagline">Money is a Derivative of Information</span>
      <svg width="16" height="26" viewBox="0 0 16 26" aria-hidden="true"><path d="M16 0 L0 13 L16 26 Z" fill="#bcbcbf"/></svg>
    </div>

    <div class="signature-labels"><span>AUTHORIZED SIGNATURE</span><span>Not Valid Unless Signed</span></div>
    <div class="signature-strip" role="img" aria-label="Handwritten signature of Delvin Ashcroft"></div>

    <div class="brand-name">TAVRO Capital Group LLC</div>
    <div class="back-contact">
      <div>555.038.6195</div>
      <div>delvin@tavrocapitalgroup.example</div>
    </div>
  </section>
</main>
</body>
</html>
```